brightvale7 Growers & Crafters Market Spring Festival

Harvest Festival Flyer. Bright Spring colors, Spring flowers, spring produce/food, Grass, Concert poster look, but legible...or MODERN LOOK- I am uploading Sponsor files that will go on bottom of flyer. I am uploading past flyers, and samples of other flyers that I like.
Flyer Info: 5x7 Size
When & Where:
April 19 9am-4pm
Marlow Commons 417 N. Bellhaven
What:
DIY workshops
Beer Truck
FREE Games & Prizes
Live Entertainment
Chef Demos
Peanut Eating Contest
FREE Kids Art Garden
BBQ
More info to come.....I have to finalize with vendors.
Sponsor Logos at Bottom:
Marlow Commons
Kikis smokehouse
brightvale7
Sol Dorado
Build Bright Paths
Green Thumb Guild
Updates

I have 2 more sponsor logos to upload.  Canine Coaching Pro & Ridgeway Brewing Company

Please add Easter Photos

please ad petting zoo

Target Market(s)

Adults 25-50

Industry/Entity Type

Festival

Requirements
Must have
• The list of items i listed above
Should not have
• County look.Make it modern

```html
<!DOCTYPE html>
<html lang="en">
<head>
<meta charset="utf-8">
<title>brightvale7 Spring Harvest Festival</title>
<link rel="stylesheet" href="https://fonts.googleapis.com/css2?family=Yellowtail&family=Playball&display=swap">
<style>
  :root {
    --page: #ffffff;
    --cream: #fdf3d4;
    --green-deep: #2f9a78;
    --green: #3fae87;
    --green-soft: #84c79d;
    --green-pale: #a9d9b5;
    --strip: #ffffff;
    --ink: #4a6a5a;
  }
  * { margin: 0; padding: 0; box-sizing: border-box; }
  html, body { width: 907px; height: 1200px; overflow: hidden; background: var(--page); }
  .canvas { position: relative; width: 907px; height: 1200px; background: var(--page); }
  .flyer {
    position: absolute; left: 78px; top: 69px; width: 752px; height: 1062px;
    background: var(--cream); overflow: hidden;
  }
  .flyer > * { position: absolute; }
  .script { font-family: "Playball", cursive; font-weight: 400; color: var(--green-soft); white-space: nowrap; }
  .brand-line { left: 0; width: 100%; top: 36px; text-align: center; font-size: 38px; }
  .market-line { left: 0; width: 100%; top: 92px; text-align: center; font-size: 38px; }
  .title {
    font-family: "Yellowtail", cursive; font-weight: 400; white-space: nowrap; line-height: 1;
  }
  .title--spring { left: 90px; top: 190px; font-size: 140px; color: var(--green); }
  .title--harvest { left: 215px; top: 318px; font-size: 140px; color: var(--green-deep); }
  .title--festival { left: 225px; top: 445px; font-size: 140px; color: var(--green); }
  .rule { left: 0; top: 0; }
  .hours {
    left: 65px; top: 478px; width: 134px; height: 134px;
    display: flex; align-items: center; justify-content: center; text-align: center;
    font-size: 32px; line-height: 1.05;
  }
  .hours svg { position: absolute; inset: 0; }
  .when { left: 280px; top: 640px; width: 390px; font-size: 34px; line-height: 1.3; text-align: right; }
  .activities { list-style: none; }
  .activities li { position: absolute; font-size: 27px; color: var(--green-pale); white-space: nowrap; padding-left: 26px; }
  .activities li::before {
    content: ""; position: absolute; left: 0; top: 50%; width: 16px; height: 6px;
    border-radius: 6px 0 6px 0; background: var(--green-pale);
  }
  .butterfly { display: block; }
  .sponsors {
    left: 53px; top: 954px; width: 646px; height: 78px; background: var(--strip);
    display: grid; grid-template-columns: repeat(6, 1fr); align-items: center; column-gap: 8px; padding: 0 10px;
  }
  .sponsor {
    font-family: "Playball", cursive; font-size: 14px; line-height: 1.15; color: var(--ink);
    display: flex; align-items: center; justify-content: center; gap: 4px; text-align: center;
  }
  .sponsor .dot { flex: none; width: 9px; height: 9px; border-radius: 50%; background: var(--green-soft); }
</style>
</head>
<body>
<div class="canvas">
  <main class="flyer">
    <svg class="flower" style="left:232px;top:45px" width="26" height="26" role="img" aria-label="Small flower ornament"><circle cx="13" cy="13" r="11" fill="var(--green)"/></svg>
    <svg class="flower" style="left:494px;top:45px" width="26" height="26" role="img" aria-label="Small flower ornament"><circle cx="13" cy="13" r="11" fill="var(--green)"/></svg>
    <p class="script brand-line">brightvale7</p>
    <p class="script market-line">Growers &amp; Crafters Market</p>

    <svg class="butterfly" style="left:626px;top:30px" width="54" height="44" role="img" aria-label="Butterfly illustration"><ellipse cx="27" cy="22" rx="26" ry="18" fill="var(--green)"/></svg>
    <svg class="butterfly" style="left:520px;top:280px" width="54" height="44" role="img" aria-label="Butterfly illustration"><ellipse cx="27" cy="22" rx="26" ry="18" fill="var(--green-soft)"/></svg>
    <svg class="butterfly" style="left:40px;top:373px" width="60" height="50" role="img" aria-label="Butterfly illustration"><ellipse cx="30" cy="25" rx="29" ry="21" fill="var(--green-pale)"/></svg>

    <h1 class="title title--spring">Spring</h1>
    <h1 class="title title--harvest">Harvest</h1>
    <h1 class="title title--festival">Festival</h1>

    <svg class="rule" width="752" height="880" aria-hidden="true">
      <line x1="272" y1="610" x2="665" y2="610" stroke="var(--green)" stroke-width="3"/>
      <circle cx="458" cy="610" r="6" fill="var(--green)"/>
      <line x1="378" y1="738" x2="665" y2="738" stroke="var(--green-soft)" stroke-width="5" stroke-dasharray="10 6"/>
    </svg>

    <div class="script hours">
      <svg width="134" height="134" aria-hidden="true"><circle cx="67" cy="67" r="63" fill="none" stroke="var(--green-soft)" stroke-width="5" stroke-dasharray="9 6"/></svg>
      <span>9am-<br>4pm</span>
    </div>

    <p class="script when">April 19 Marlow Commons<br>417 N. Bellhaven</p>

    <ul class="script activities">
      <li style="left:68px;top:668px">BBQ</li>
      <li style="left:40px;top:716px">DIY Workshops</li>
      <li style="left:40px;top:764px">Free Games &amp; Prizes</li>
      <li style="left:48px;top:812px">Free Kids Art Garden</li>
      <li style="left:50px;top:860px">Peanut Eating Contest</li>
      <li style="left:420px;top:764px">Beer Truck</li>
      <li style="left:420px;top:812px">Chef Demos</li>
      <li style="left:420px;top:860px">Live Entertainment</li>
      <li style="left:420px;top:904px">www.brightvale7.com</li>
    </ul>

    <div class="sponsors">
      <span class="sponsor"><span class="dot"></span>brightvale7</span>
      <span class="sponsor">Sol Dorado</span>
      <span class="sponsor">Kikis smokehouse</span>
      <span class="sponsor">Green Thumb Guild</span>
      <span class="sponsor">Build Bright Paths</span>
      <span class="sponsor">Marlow Commons</span>
    </div>
  </main>
</div>
</body>
</html>
```